IT Company that provides secure IT solutions and services to our customers

We need business cards and a logo for a new IT Solutions company just created based in Kuala Lumpur, Malaysia. But will also be serving other countries in the region. We provide secure data, voice solutions on mobile platforms. Our first offering is encrypted voice and data solutions for ZUN, Pellovan, Quillet and Frondmoss devices.

Target Market(s)

large organizations Govt, Police, Defence, Anti-corruption, Legal, highly regulated industries such as Health-care, Financial, Banking, Insurance,

Industry/Entity Type

Information Technology

Contact Information for Business Card

VorlexIT (Logo - colour is ORVA blue)Rashid Nawfal Managing Director Kryption IT Sdn. Bhd.3rd Floor, Block C, Wisma LPN,No.14 Jalan Seri Hamzani,58410, Kuala LumpurMalaysia

Font styles to use
Sans Serif

Colors
3176b5
ec1f27
fbed22

Requirements
Must have
• VorlexIT all in Blue like ORVA blue. A logo design perhaps a play of VI, K with a dangling T (colour can be any)
Nice to have
• I want a clean crisp card, not too busy, easy to read.

```html
<!DOCTYPE html>
<html lang="en">
<head>
<meta charset="utf-8">
<title>VorlexIT Business Card</title>
<link rel="stylesheet" href="https://fonts.googleapis.com/css2?family=Archivo+Black&family=Open+Sans:wght@400;700&display=swap">
<style>
  :root {
    --backdrop: #2c2e33;
    --card: #ffffff;
    --ink: #1b1b1b;
    --brand-blue: #3176b5;
    --accent: #d7232b;
    --accent-faint: #f9e1e1;
    --rule: #d9d9d9;
  }
  * { margin: 0; padding: 0; box-sizing: border-box; }
  html, body {
    width: 1200px;
    height: 864px;
    overflow: hidden;
    background: var(--backdrop);
  }
  .canvas {
    position: relative;
    width: 1200px;
    height: 864px;
  }
  .card {
    position: absolute;
    width: 560px;
    height: 320px;
    background: var(--card);
    overflow: hidden;
    box-shadow: 0 6px 18px rgba(0,0,0,0.35);
  }
  .card--front { left: 330px; top: 80px; }
  .card--back { left: 250px; top: 460px; }

  .front-lockup {
    position: absolute;
    inset: 0;
    display: flex;
    align-items: center;
    justify-content: center;
    gap: 14px;
  }
  .brand-dot {
    width: 40px;
    height: 40px;
    border: 3px solid var(--accent);
    border-radius: 50%;
  }
  .brand-divider {
    width: 1px;
    height: 40px;
    background: var(--rule);
  }
  .brand-name {
    font-family: "Archivo Black", sans-serif;
    font-size: 40px;
    letter-spacing: 0.5px;
    color: var(--brand-blue);
    text-transform: uppercase;
    line-height: 1;
    white-space: nowrap;
  }

  .back-brand {
    position: absolute;
    left: 40px;
    top: 36px;
    font-size: 46px;
  }
  .back-mark {
    position: absolute;
    right: -70px;
    bottom: -90px;
    width: 300px;
    height: 300px;
  }
  .contact {
    position: absolute;
    left: 40px;
    top: 130px;
    font-family: "Open Sans", sans-serif;
    color: var(--ink);
  }
  .contact__name {
    font-weight: 700;
    font-size: 15px;
    color: var(--accent);
  }
  .contact__role {
    font-size: 13px;
    margin-bottom: 20px;
  }
  .contact__company {
    font-weight: 700;
    font-size: 15px;
    color: var(--accent);
  }
  .contact__address {
    font-size: 13px;
    line-height: 1.35;
    font-style: normal;
  }
</style>
</head>
<body>
<main class="canvas">
  <section class="card card--front" aria-label="Business card front">
    <div class="front-lockup">
      <span class="brand-dot" aria-hidden="true"></span>
      <span class="brand-divider" aria-hidden="true"></span>
      <span class="brand-name">VorlexIT</span>
    </div>
  </section>

  <section class="card card--back" aria-label="Business card back">
    <svg class="back-mark" viewBox="0 0 300 300" aria-hidden="true">
      <circle cx="150" cy="150" r="135" fill="none" stroke="var(--accent-faint)" stroke-width="18"/>
    </svg>
    <div class="brand-name back-brand">VorlexIT</div>
    <div class="contact">
      <p class="contact__name">Rashid Nawfal</p>
      <p class="contact__role">Managing Director</p>
      <p class="contact__company">Vorlex IT</p>
      <address class="contact__address">
        Sdn. Bhd.3rd Floor, Block C, &nbsp;Wisma<br>
        LPN,No.14 Jalan Seri Hamzani, 58410,<br>
        Kuala Lumpur Malaysia
      </address>
    </div>
  </section>
</main>
</body>
</html>
```